Artist needs a Wordpress Website design to market my original paintings

Mira Castellan Gallery.com
Artist - Original Abstract Paintings

Artist needs classy and elegant WORDPRESS website to market my Original Paintings.
What sets these paintings apart?
Each one was inspired by the inner connection between the artist and the individual destined to receive the painting. Paintings are priced high end and require a website to reflect their high quality.
Website must be responsive on all devices. eg. mobile, laptop and desktop. It must have a shopping cart in order to complete sales.
The domain name miracastellangallery.com has already been purchased and is hosted on Corvanet.
I want it to be very easy to navigate and also easy for me to add and edit more images and content.
I have no official logo but you can insert the title,
Mira Castellan
Collection
Original Fluid Art Paintings
in whatever design/font format you feel attractive, I leave that to the designer. I want it to be simple and include a lot of negative space to avoid a cluttered look. The paintings are colorful on their own and prefer not to detract from them as a focal point. I leave the color theme to the designer. Perhaps you may like to extract a color theme from one of the paintings.
Requirements:
5 pages: HOME, ABOUT, SHOP, CART, CONTACT
Home page:
-Menu across the top
-1 large painting (prefer the purple and green painting)
-3 smaller images below the large one
Unless you come up with a more professional format.
ABOUT:
(You can include my uploaded photo for now on the ABOUT page. I will replace it when I get a professional photo.)
I learned I am never too old to re-invent my life. Lesson learned. At the age of 78 and after the ending of my 30 years of marriage I was faced with an unexpected change in my life circumstances. I made the decision to re-invent my life.
Art, in varying media has always been a part of my experience as a hobby. When I was presented with fluid art, my life as I had known it turned to excitement, and discovery, carving a promising vision of my future.
My spiritual training has taught me how to recognize my connection with people inwardly. With this awareness it became clear to me while painting that I was creating a work of art for a specific individual. I allow creative expression to flow through me that is destined for you. I do not know who you are, but if you recognize the painting that inspires you, I have succeeded with our connection.
I live in Washington State, USA
I am looking forward to meeting you.
Mira Castellan
SHOP:
This should be the gallery from which one can shop. The images will be more like a thumbprint but large enough to see well, perhaps 3 across the page. As one hovers over, or clicks on one, it will link to a page with a larger view that has:
-Description
-Price and a CHOICE to click on
-Add to Cart Button OR
-Continue shopping (so they don't have to go back to homepage)
This page should be a scrolling one so eventually all of my paintings will be added to this page and easy for someone to shop instead of going back and forth between pages.
Please set this up (making it a link to larger image, etc) and include one or all of the images I upload here. I will add the rest.

CART:
-Add a shopping cart

CONTACT:
-email: castellangallery@mailvessel.net
All pages should have a link back to the homepage.
SOCIAL MEDIA LINKS:
-Pictaro:
http://pictaro.example/miracastellangallery
-Socialroom
https://www.socialroom.example/theuniquecanvas/?
view_public_for=384751029366217

http://ellisbrookstudio.net
eg of a website that I like the navigation. I like the simplicity of the Home Page but the photo is too large. A smaller main photo and 3 smaller ones beneath it would have looked nicer to me.

```html
<!DOCTYPE html>
<html lang="en">
<head>
<meta charset="utf-8">
<title>Mira Castellan Collection — Home</title>
<link rel="stylesheet" href="https://fonts.googleapis.com/css2?family=Lato:wght@400;700&family=Great+Vibes&display=swap">
<style>
  :root {
    --ink: #141414;
    --accent-green: #3fcf8e;
    --plum: #5e2750;
    --plum-line: #6b2c5c;
    --footer-bg: #3b3b3b;
    --white: #ffffff;
  }
  * { box-sizing: border-box; margin: 0; padding: 0; }
  html, body { width: 1200px; height: 1055px; overflow: hidden; background: var(--white); }
  body { position: relative; font-family: "Lato", Arial, sans-serif; color: var(--ink); }

  .site-header { position: absolute; left: 0; top: 0; width: 1200px; height: 77px; background: var(--white); }
  .brand { position: absolute; left: 111px; top: 24px; font-size: 20px; font-weight: 700; color: var(--ink); letter-spacing: 0.3px; white-space: nowrap; }
  .main-nav { position: absolute; top: 29px; left: 0; width: 100%; }
  .main-nav a { position: absolute; font-size: 15px; font-weight: 700; color: var(--ink); text-decoration: none; line-height: 18px; }
  .main-nav a.is-active { color: var(--accent-green); font-weight: 400; }
  .main-nav a.is-active::after { content: ""; position: absolute; left: 0; right: 0; top: 22px; height: 2px; background: var(--accent-green); }
  .cart-link { position: absolute; left: 845px; top: 18px; width: 40px; height: 40px; border: 1.5px solid var(--plum-line); border-radius: 50%; }
  .cart-link svg { position: absolute; left: 10px; top: 11px; }
  .cart-count { position: absolute; left: 873px; top: 11px; width: 20px; height: 20px; border-radius: 50%; background: var(--accent-green); color: var(--white); font-size: 13px; font-weight: 700; text-align: center; line-height: 20px; }
  .shop-button { position: absolute; left: 948px; top: 16px; width: 141px; height: 46px; border-radius: 23px; background: var(--plum); color: var(--white); font-size: 14.5px; font-weight: 700; text-decoration: none; display: flex; align-items: center; justify-content: center; gap: 10px; }

  .hero { position: absolute; left: 0; top: 77px; width: 1200px; height: 581px;
    background:
      radial-gradient(ellipse 420px 260px at 720px 170px, #3fe08a 0%, rgba(63,224,138,0) 70%),
      radial-gradient(ellipse 380px 300px at 380px 470px, #8a5a9a 0%, rgba(138,90,154,0) 75%),
      linear-gradient(135deg, #2f6a3c 0%, #4a8f4a 25%, #6a3c78 50%, #3fb878 70%, #2c2540 100%); }
  .hero-title { position: absolute; left: 0; top: 228px; width: 100%; text-align: center; font-family: "Great Vibes", cursive; font-size: 92px; font-weight: 400; color: var(--white); line-height: 1; }

  .gallery-row { position: absolute; top: 665px; left: 111px; display: flex; gap: 10px; }
  .gallery-tile { width: 320px; height: 239px; }
  .tile-bloom { background: linear-gradient(135deg, #c48a3a 0%, #7b3f6a 45%, #2e4a6a 70%, #d9b24a 100%); }
  .tile-garden { background: linear-gradient(135deg, #8a2a3a 0%, #b44a4a 40%, #3e6a4a 70%, #c06070 100%); }
  .tile-amber { background: linear-gradient(135deg, #c7742a 0%, #e8cfa8 45%, #b85a22 75%, #f0e4d0 100%); }

  .site-footer { position: absolute; left: 0; top: 969px; width: 1200px; height: 86px; background: var(--footer-bg); color: var(--white); }
  .footer-mail { position: absolute; left: 113px; top: 24px; width: 38px; height: 38px; border: 1.5px solid var(--white); border-radius: 50%; }
  .footer-mail svg { position: absolute; left: 9px; top: 11px; }
  .footer-email { position: absolute; left: 173px; top: 33px; font-size: 15.5px; color: var(--white); text-decoration: none; line-height: 18px; }
  .social-list { position: absolute; left: 490px; top: 24px; display: flex; gap: 8px; list-style: none; }
  .social-list a { display: flex; align-items: center; justify-content: center; width: 38px; height: 38px; border: 1.5px solid var(--white); border-radius: 50%; color: var(--white); text-decoration: none; font-size: 7px; font-weight: 700; }
  .copyright { position: absolute; right: 111px; top: 33px; font-size: 15.5px; line-height: 18px; }
</style>
</head>
<body>
  <header class="site-header">
    <a class="brand">Mira Castellan Collection</a>
    <nav class="main-nav">
      <a class="is-active" style="left:495px">HOME</a>
      <a style="left:571px">ABOUT</a>
      <a style="left:652px">SHOP</a>
      <a style="left:723px">CONTACT</a>
    </nav>
    <a class="cart-link" aria-label="Cart">
      <svg width="18" height="16" viewBox="0 0 18 16"><path d="M0 1h3l2 9h10l2-7H4.5" fill="none" stroke="#3fcf8e" stroke-width="2" stroke-linejoin="round"/><path d="M5 3h12l-2 7H5z" fill="#3fcf8e"/><circle cx="6.5" cy="14" r="1.6" fill="#3fcf8e"/><circle cx="13.5" cy="14" r="1.6" fill="#3fcf8e"/></svg>
    </a>
    <span class="cart-count">0</span>
    <a class="shop-button">SHOP ART
      <svg width="14" height="12" viewBox="0 0 18 16"><path d="M0 1h3l2 9h10l2-7H4.5" fill="none" stroke="#fff" stroke-width="2"/><path d="M5 3h12l-2 7H5z" fill="#fff"/><circle cx="6.5" cy="14" r="1.6" fill="#fff"/><circle cx="13.5" cy="14" r="1.6" fill="#fff"/></svg>
    </a>
  </header>

  <section class="hero" role="img" aria-label="Featured purple and green fluid art painting">
    <h1 class="hero-title">Original Paintings</h1>
  </section>

  <section class="gallery-row">
    <div class="gallery-tile tile-bloom" role="img" aria-label="Fluid art painting with a multicolour bloom on gold and plum"></div>
    <div class="gallery-tile tile-garden" role="img" aria-label="Fluid art painting with cream and green florals on deep red"></div>
    <div class="gallery-tile tile-amber" role="img" aria-label="Fluid art painting with amber and white cells"></div>
  </section>

  <footer class="site-footer">
    <span class="footer-mail"><svg width="18" height="14" viewBox="0 0 18 14"><rect x="1" y="1" width="16" height="12" rx="2" fill="none" stroke="#fff" stroke-width="1.8"/><path d="M1.5 2l7.5 6 7.5-6" fill="none" stroke="#fff" stroke-width="1.8"/></svg></span>
    <a class="footer-email">castellangallery@mailvessel.net</a>
    <ul class="social-list">
      <li><a>Room</a></li>
      <li><a>Chirp</a></li>
      <li><a>Pictaro</a></li>
      <li><a>Vid</a></li>
      <li><a>Feed</a></li>
    </ul>
    <p class="copyright">© 2020 Mira Castellan. All Rights Reserved</p>
  </footer>
</body>
</html>
```